Full Page Ad for Coastal Dwelling Journal

we are The Garden Quarter an Outdoor design and construction company form Miami. see our website to get a better idea of who we are, what we do and our company profile. www.thegardenquarter-example.com

we need a full page ad for a luxury construction an architecture magazine. see magazine profile http://www.coastaldwelling-example.com/

design requirements:

use a minimum of 1 images or a maximum of 4 images from the files available

include Logo ( obviously )

include following text ( in no particular order):
"Outdoor Design & Construction / Outdoor Furniture "
"we create unique outdoor living spaces"
"thegardenquarter-example.com"
"Showroom: 4120 NW 62 Ave Miami, FL 33166"
"786.555.0142"

From the files uploaded see examples of ads that we like.

Specs:
Full Page
Final Trim : 8" x 10-7/8"
Live Area ( type) 7" x 10"
Bleed: 8.25" x 11.125"
Decimal equivalents: 8" x 10.875"

Reason: Really like the designs guys just want to see a few more options using some of the images that haven't been used yet. particularly the white structure attached to the house. thanks, TGQ Marketing team

```html
<!DOCTYPE html>
<html lang="en">
<head>
<meta charset="utf-8">
<title>The Garden Quarter — Full Page Ad</title>
<link href="https://fonts.googleapis.com/css2?family=Josefin+Sans:wght@300;400&family=Josefin+Slab:wght@400&family=Arimo:wght@400&display=swap" rel="stylesheet">
<style>
  :root {
    --paper: #ffffff;
    --ink: #1f1f1f;
    --muted: #8a8a8a;
    --teal: #4a9fa3;
    --sky-top: #dfe6ec;
    --sky-low: #c9d8e2;
    --foliage: #4f6b3a;
    --pool: #8fd3d6;
    --deck: #e6d6c2;
    --inset-light: #eef3f3;
    --inset-deep: #6f9598;
    --mark: #3f9b8a;
  }
  * { margin: 0; padding: 0; box-sizing: border-box; }
  html, body { width: 927px; height: 1200px; overflow: hidden; background: var(--paper); }
  .ad { position: relative; width: 927px; height: 1200px; background: var(--paper); overflow: hidden; }

  .hero-photo {
    position: absolute; left: 0; top: 0; width: 927px; height: 873px;
    background: linear-gradient(180deg,
      var(--sky-top) 0%, var(--sky-low) 38%,
      var(--foliage) 46%, #7b8f66 52%,
      var(--pool) 60%, #a9dcdc 70%,
      var(--deck) 78%, #e9ddd0 100%);
  }

  .wordmark { position: absolute; left: 0; top: 0; width: 927px; height: 900px; }
  .wordmark .big { font-family: "Josefin Slab", serif; font-size: 300px; fill: var(--paper); }
  .wordmark .arc-text { font-family: "Josefin Sans", sans-serif; font-weight: 400; font-size: 30px; letter-spacing: 4px; fill: var(--teal); }

  .tagline {
    position: absolute; top: 897px; left: 0; width: 927px; text-align: center;
    font-family: "Josefin Sans", sans-serif; font-weight: 300; font-size: 25px;
    letter-spacing: 15px; color: var(--muted); padding-left: 15px;
  }
  .services {
    position: absolute; top: 942px; left: 0; width: 927px; text-align: center;
    font-family: "Josefin Sans", sans-serif; font-weight: 400; font-size: 17.5px;
    letter-spacing: 1px; color: var(--ink);
  }

  .showroom {
    position: absolute; left: 54px; top: 1107px;
    font-family: "Arimo", sans-serif; font-size: 13px; line-height: 19px; color: var(--ink);
  }
  .website {
    position: absolute; left: 340px; top: 1129px; width: 240px; text-align: center;
    font-family: "Arimo", sans-serif; font-size: 14px; letter-spacing: 1px; color: var(--ink);
  }
  .brand { position: absolute; left: 636px; top: 1112px; display: flex; align-items: center; gap: 10px; }
  .brand-dot { width: 44px; height: 44px; border-radius: 50%; background: var(--mark); }
  .brand-name {
    font-family: "Josefin Sans", sans-serif; font-weight: 400; font-size: 17px;
    letter-spacing: 0.5px; color: #2b2b2b; text-transform: uppercase;
  }
</style>
</head>
<body>
<main class="ad">
  <div class="hero-photo" role="img" aria-label="Photo of a resort-style backyard pool with a beach entry, stone deck, a white-curtained pergola with outdoor kitchen, and tall royal palms under a cloudy sky"></div>

  <svg class="wordmark" viewBox="0 0 927 900" aria-label="We create unique">
    <defs>
      <clipPath id="inset-clip"><circle cx="511" cy="755" r="114"/></clipPath>
      <linearGradient id="inset-fill" x1="0" y1="0" x2="0" y2="1">
        <stop offset="0" stop-color="var(--inset-light)"/>
        <stop offset="0.45" stop-color="#cfdede"/>
        <stop offset="1" stop-color="var(--inset-deep)"/>
      </linearGradient>
      <path id="arc-path" d="M 412 656 A 140 140 0 0 1 643 707"/>
    </defs>

    <text class="big" x="-6" y="873" textLength="398" lengthAdjust="spacingAndGlyphs">uni</text>
    <text class="big" x="615" y="873" textLength="330" lengthAdjust="spacingAndGlyphs">ue</text>

    <rect x="397" y="641" width="228" height="228" fill="url(#inset-fill)" clip-path="url(#inset-clip)" role="img" aria-label="Photo of a modern outdoor lounge set with white cushions and a glass coffee table on a terrace"/>
    <circle cx="511" cy="755" r="114" fill="none" stroke="var(--paper)" stroke-width="9"/>
    <line x1="530" y1="800" x2="608" y2="873" stroke="var(--paper)" stroke-width="16"/>

    <text class="arc-text"><textPath href="#arc-path">WE CREATE</textPath></text>
  </svg>

  <p class="tagline">OUTDOOR LIVING SPACES</p>
  <p class="services">OUTDOOR DESIGN &amp; CONSTRUCTION / OUTDOOR FURNITURE</p>

  <address class="showroom" style="font-style: normal;">
    Showroom:<br>
    4120 NW 62 Ave Miami, FL 33166<br>
    786.555.0142
  </address>
  <p class="website">thegardenquarter-example.com</p>
  <div class="brand">
    <span class="brand-dot"></span>
    <span class="brand-name">The Garden Quarter</span>
  </div>
</main>
</body>
</html>
```